Brindmoor Gardening Fresh New Website

We are looking to create a simple fresh website for our landscaping business. The website should appeal to a 'high end' audience. We deal with a lot of Embassies and affluent clients who have extremely large gardens that are meticulously maintained. The site is about communicating our excellent landscaping and customer service skills and encouraging new clients to reach out and engage us to take care of their gardens.

The website is basically going to be our business card, it will have almost no functionality other than two 'contact us' forms, one for smaller clients and one for more detailed projects.

The website will not have a lot of written content and will have to show photos of beautifully landscaped gardens.

The main logo in black will influence the site, however, we are open to all suggestions.

We are expecting to have the following pages:
Home Page
Services
About Us
Contact Us
Showcase (photo gallery of our work)

We need someone who can code it to wordpress and be available for minor changes over a number of days. They will be simple tweaks.

```html
<!DOCTYPE html>
<html lang="en">
<head>
<meta charset="utf-8">
<title>Brindmoor Gardening</title>
<link href="https://fonts.googleapis.com/css2?family=Libre+Baskerville:wght@400;700&family=Roboto:wght@400;500;700&display=swap" rel="stylesheet">
<style>
:root{
  --gold:#b3832a;
  --gold-dark:#9b6f1f;
  --gold-light:#e9c54e;
  --ink:#1b1a17;
  --text:#5a5a5a;
  --white:#ffffff;
  --field:#d9d9d9;
}
*{margin:0;padding:0;box-sizing:border-box}
html,body{width:1200px;height:4000px;overflow:hidden;background:var(--white);font-family:"Roboto",Arial,sans-serif;color:var(--text)}
.page{position:relative;width:1200px;height:4000px;overflow:hidden}
.serif{font-family:"Libre Baskerville",Georgia,serif}
.backdrop{position:absolute;left:0;top:0}
/* header */
.site-header{position:absolute;left:0;top:0;width:1200px;height:80px;background:var(--ink)}
.brand{position:absolute;left:118px;top:22px;width:140px;color:var(--gold-light);font-family:"Libre Baskerville",Georgia,serif;font-size:12px;letter-spacing:3px;line-height:18px;text-align:center;white-space:nowrap}
.nav{position:absolute;left:325px;top:32px;display:flex;gap:22px;font-size:13px;font-weight:500;color:var(--white);white-space:nowrap}
.nav .active{color:var(--gold-light)}
.socials{position:absolute;left:741px;top:27px;display:flex;gap:5px}
.socials span{width:27px;height:27px;border:1.5px solid var(--white);border-radius:50%}
.divider{position:absolute;left:850px;top:16px;width:1px;height:48px;background:#666}
.call{position:absolute;left:872px;top:18px}
.call-text{position:absolute;left:920px;top:20px;color:var(--gold-light);font-size:12px;white-space:nowrap}
.call-text b{display:block;color:var(--white);font-size:17px;margin-top:3px}
/* hero */
.hero-photo{position:absolute;left:0;top:80px;width:1200px;height:700px;background:linear-gradient(180deg,#4f5a3c 0%,#6d7a4a 30%,#4a7a2a 55%,#6fa234 100%)}
.hero-title{position:absolute;left:141px;top:228px;color:var(--white);font-size:68px;font-weight:700;line-height:1;white-space:nowrap}
.hero-sub{position:absolute;left:141px;top:315px;color:var(--white);font-size:40px;font-weight:700;white-space:nowrap}
.btn{display:flex;align-items:center;justify-content:center;border-radius:24px;background:linear-gradient(90deg,var(--gold) 0%,var(--gold-light) 100%);color:var(--ink);font-size:13px;font-weight:700;text-transform:uppercase}
.hero-btn{position:absolute;left:141px;top:373px;width:156px;height:46px}
.dots{position:absolute;left:141px;top:555px;display:flex;gap:10px}
.dots span{width:40px;height:40px;border-radius:50%;background:var(--white)}
.quote{position:absolute;left:694px;top:152px;width:362px;height:438px;background:var(--white);padding:26px 24px}
.quote h2{text-align:center;color:var(--gold);font-size:34px;font-weight:700;margin-bottom:16px;white-space:nowrap}
.field{border:1px solid #cfcfcf;height:42px;margin-bottom:6px;padding:12px 14px;font-size:13px;color:#777;background:var(--white)}
.quote .msg{height:122px}
.quote .btn{width:155px;height:46px;margin:8px auto 0}
/* services */
.section-title{position:absolute;width:1200px;text-align:center;font-size:36px;font-weight:700}
.svc{position:absolute;top:982px;width:260px;height:450px}
.svc-title{position:absolute;top:270px;width:100%;text-align:center;color:#222;font-size:23px;font-weight:500}
.svc-copy{position:absolute;top:310px;left:30px;width:200px;text-align:center;font-size:13px;line-height:20px;color:#666}
.side-arrow{position:absolute;top:1187px}
/* about */
.badge{position:absolute;left:121px;top:1687px;width:203px;height:92px;background:var(--gold);color:var(--white)}
.badge b{position:absolute;left:18px;top:16px;font-family:"Libre Baskerville",Georgia,serif;font-size:50px;font-weight:400}
.badge span{position:absolute;left:88px;top:22px;font-size:15px;line-height:24px}
.frame{position:absolute;left:234px;top:1799px;width:368px;height:307px;border:4px solid var(--gold)}
.about-photo{position:absolute;left:144px;top:1723px;width:435px;height:358px;background:linear-gradient(180deg,#a8c3dc 0%,#b99a74 38%,#6d4a32 60%,#5d8a34 100%)}
.about-title{position:absolute;left:638px;top:1717px;color:var(--gold);font-size:36px;font-weight:700}
.about-copy{position:absolute;left:638px;top:1773px;width:416px;font-size:13px;line-height:19.8px;text-align:justify;color:#666}
.about-btn{position:absolute;left:638px;top:2034px;width:154px;height:45px;color:var(--white)}
/* contact */
.contact-title{color:var(--white);top:2345px}
.cfield{position:absolute;height:46px;background:var(--white);padding:15px 16px;font-size:13px;color:#666}
.contact-submit{position:absolute;left:526px;top:2670px;width:155px;height:46px;background:#f0c419;border-radius:24px}
/* gallery */
.gallery-title{color:var(--gold);top:2983px}
.shot{position:absolute}
/* footer */
.footer-brand{position:absolute;left:170px;top:3820px;width:240px;text-align:center;color:var(--gold-light);font-family:"Libre Baskerville",Georgia,serif;font-size:20px;letter-spacing:6px;line-height:30px;white-space:nowrap}
.footer-brand small{display:block;font-size:12px;letter-spacing:6px}
.fcol{position:absolute;top:3725px;color:var(--white)}
.fcol h4{font-family:"Libre Baskerville",Georgia,serif;font-size:16px;font-weight:700;margin-bottom:18px;white-space:nowrap}
.fcol li{list-style:none;font-size:13px;line-height:20px}
.contact-item{display:flex;gap:10px;font-size:13px;line-height:20px;margin-bottom:16px;align-items:flex-start}
.contact-item i{flex:none;width:30px;height:30px;border-radius:50%;background:linear-gradient(90deg,var(--gold),var(--gold-light));display:flex;align-items:center;justify-content:center}
.rule{position:absolute;left:196px;top:3943px;width:806px;height:1px;background:#444}
.copyright{position:absolute;top:3960px;width:1200px;text-align:center;color:var(--white);font-size:12px}
</style>
</head>
<body>
<div class="page">

  <div class="hero-photo" role="img" aria-label="Photo of a stone house with a manicured front lawn and flower beds"></div>

  <svg class="backdrop" width="1200" height="4000" viewBox="0 0 1200 4000" aria-hidden="true">
    <defs>
      <linearGradient id="goldband" x1="0" y1="0" x2="1" y2="1">
        <stop offset="0" stop-color="#b3832a"/><stop offset="1" stop-color="#a97a22"/>
      </linearGradient>
      <linearGradient id="shine" x1="0" y1="0" x2="1" y2="0">
        <stop offset="0" stop-color="#b3832a"/><stop offset="1" stop-color="#f2d35a"/>
      </linearGradient>
      <linearGradient id="contactband" x1="0" y1="0" x2="1" y2="1">
        <stop offset="0" stop-color="#b98a30"/><stop offset="0.5" stop-color="#c39437"/><stop offset="1" stop-color="#ab7c25"/>
      </linearGradient>
    </defs>
    <polygon points="600,763 1200,668 1200,652 600,776 0,652 0,1487 600,1590 1200,1487 1200,652" fill="url(#shine)"/>
    <polygon points="0,652 600,776 1200,670 1200,1487 600,1590 0,1487" fill="url(#goldband)"/>
    <polygon points="330,915 450,950 450,1030 330,1060" fill="#a67720" opacity="0.6"/>
    <polygon points="750,950 870,915 870,1060 750,1030" fill="#a67720" opacity="0.6"/>
    <polygon points="330,1440 450,1390 520,1440 520,1540 330,1540" fill="#a67720" opacity="0.45"/>
    <polygon points="680,1440 750,1390 870,1440 870,1540 680,1540" fill="#a67720" opacity="0.45"/>
    <polygon points="0,2312 600,2199 1200,2312 1200,2763 600,2863 0,2763" fill="url(#contactband)" role="img" aria-label="Faint mountain landscape photo tinted gold"/>
    <polygon points="0,2300 600,2190 1200,2300 1200,2312 600,2199 0,2312" fill="#d7a83d"/>
    <polygon points="0,3694 600,3565 1200,3694 1200,4000 0,4000" fill="url(#shine)"/>
    <polygon points="0,3704 600,3584 1200,3704 1200,4000 0,4000" fill="#1b1a17"/>
  </svg>

  <header class="site-header">
    <div class="brand">BRINDMOOR<br>GARDENING</div>
    <nav class="nav">
      <span class="active">HOME</span><span>SERVICES</span><span>ABOUT US</span><span>CONTACT US</span><span>SHOWCASE</span>
    </nav>
    <div class="socials"><span></span><span></span><span></span></div>
    <div class="divider"></div>
    <svg class="call" width="40" height="40" viewBox="0 0 24 24" aria-hidden="true">
      <path d="M6.6 10.8a15.1 15.1 0 0 0 6.6 6.6l2.2-2.2c.3-.3.7-.4 1-.2 1.1.4 2.3.6 3.6.6.6 0 1 .4 1 1V20c0 .6-.4 1-1 1A17 17 0 0 1 3 4c0-.6.4-1 1-1h3.5c.6 0 1 .4 1 1 0 1.3.2 2.5.6 3.6.1.3 0 .7-.2 1z" fill="#e9c54e"/>
    </svg>
    <div class="call-text">CALL US :<b>+1 555 204 7719</b></div>
  </header>

  <h1 class="hero-title serif">BRINDMOOR</h1>
  <div class="hero-sub serif">GARDENING</div>
  <div class="btn hero-btn">Get Started</div>
  <div class="dots"><span></span><span></span></div>

  <form class="quote">
    <h2 class="serif">GET A QUOTE</h2>
    <div class="field">Name</div>
    <div class="field">Email</div>
    <div class="field">Phone</div>
    <div class="field msg">Message</div>
    <div class="btn">Submit Now</div>
  </form>

  <h2 class="section-title serif" style="top:885px;color:#fff">OUR SERVICES</h2>

  <svg class="side-arrow" style="left:0" width="62" height="80" viewBox="0 0 62 80" aria-hidden="true">
    <polygon points="0,0 44,0 62,40 44,80 0,80" fill="#2a2723"/>
    <polyline points="28,30 18,40 28,50" fill="none" stroke="#fff" stroke-width="3"/>
  </svg>
  <svg class="side-arrow" style="left:1138px" width="62" height="80" viewBox="0 0 62 80" aria-hidden="true">
    <polygon points="62,0 18,0 0,40 18,80 62,80" fill="#2a2723"/>
    <polyline points="34,30 44,40 34,50" fill="none" stroke="#fff" stroke-width="3"/>
  </svg>

  <div class="svc" style="left:166px">
    <svg width="260" height="450" viewBox="0 0 260 450">
      <polygon points="130,0 260,62 260,388 130,450 0,388 0,62" fill="#fff"/>
      <polygon points="130,14 246,70 246,180 130,248 14,180 14,70" fill="#5e7d3a" role="img" aria-label="Photo of a gardener rolling out fresh turf"/>
      <polygon points="130,378 152,390 152,414 130,426 108,414 108,390" fill="url(#shine)"/>
      <text x="130" y="407" fill="#fff" font-size="12" text-anchor="middle" font-family="Roboto,Arial,sans-serif">»</text>
    </svg>
    <div class="svc-title">Duis aute irure</div>
    <div class="svc-copy">Lorem ipsum dolor sit amet, consectetur adipiscing elit, sed do eiusmod tempor</div>
  </div>
  <div class="svc" style="left:470px">
    <svg width="260" height="450" viewBox="0 0 260 450">
      <polygon points="130,0 260,62 260,388 130,450 0,388 0,62" fill="#fff"/>
      <polygon points="130,14 246,70 246,180 130,248 14,180 14,70" fill="#6d8a45" role="img" aria-label="Photo of planted garden beds beside a brick path"/>
      <polygon points="130,378 152,390 152,414 130,426 108,414 108,390" fill="url(#shine)"/>
      <text x="130" y="407" fill="#fff" font-size="12" text-anchor="middle" font-family="Roboto,Arial,sans-serif">»</text>
    </svg>
    <div class="svc-title">Duis aute irure</div>
    <div class="svc-copy">Lorem ipsum dolor sit amet, consectetur adipiscing elit, sed do eiusmod tempor</div>
  </div>
  <div class="svc" style="left:774px">
    <svg width="260" height="450" viewBox="0 0 260 450">
      <polygon points="130,0 260,62 260,388 130,450 0,388 0,62" fill="#fff"/>
      <polygon points="130,14 246,70 246,180 130,248 14,180 14,70" fill="#4e8a2c" role="img" aria-label="Aerial photo of a lawn with a winding stepping-stone path"/>
      <polygon points="130,378 152,390 152,414 130,426 108,414 108,390" fill="url(#shine)"/>
      <text x="130" y="407" fill="#fff" font-size="12" text-anchor="middle" font-family="Roboto,Arial,sans-serif">»</text>
    </svg>
    <div class="svc-title">Duis aute irure</div>
    <div class="svc-copy">Lorem ipsum dolor sit amet, consectetur adipiscing elit, sed do eiusmod tempor</div>
  </div>

  <div class="frame"></div>
  <div class="about-photo" role="img" aria-label="Photo of a modern home with a landscaped rock and flower garden"></div>
  <div class="badge"><b>20</b><span>YEARS<br>EXPERIENCES</span></div>
  <h2 class="about-title serif">ABOUT US</h2>
  <p class="about-copy">Lorem ipsum dolor sit amet, consectetur adipiscing elit, sed do eiusmod tempor incididunt ut labore et dolore magna aliqua. Ut enim ad minim veniam, quis nostrud exercitation ullamco laboris nisi ut aliquip ex ea commodo consequat. Duis aute irure dolor in reprehenderit in voluptate velit esse cillum dolore eu fugiat nulla pariatur. Excepteur sint occaecat cupidatat non proident, sunt in culpa qui officia deserunt mollit anim id est laborum. Lorem ipsum dolor sit amet, consectetur adipiscing elit, sed do eiusmod tempor incididunt ut labore et dolore magna aliqua. Ut enim ad minim veniam, quis nostrud exercitation ullamco laboris nisi ut aliquip ex ea commodo consequat. Duis aute irure dolor in reprehenderit in voluptate velit esse cillum dolore eu fugiat nulla pariatur.</p>
  <div class="btn about-btn">Learn More</div>

  <h2 class="section-title serif contact-title">CONTACT US</h2>
  <div class="cfield" style="left:231px;top:2406px;width:238px">Name</div>
  <div class="cfield" style="left:486px;top:2406px;width:237px">Email</div>
  <div class="cfield" style="left:740px;top:2406px;width:238px">Phone</div>
  <div class="cfield" style="left:231px;top:2468px;width:365px">Choose your services for
    <svg style="position:absolute;right:16px;top:20px" width="9" height="5" viewBox="0 0 9 5" aria-hidden="true"><polygon points="0,0 9,0 4.5,5" fill="#555"/></svg>
  </div>
  <div class="cfield" style="left:613px;top:2468px;width:365px">Date
    <svg style="position:absolute;right:14px;top:15px" width="14" height="14" viewBox="0 0 14 14" aria-hidden="true"><rect x="1" y="2" width="12" height="11" fill="none" stroke="#777"/><rect x="1" y="2" width="12" height="3" fill="#777"/></svg>
  </div>
  <div class="cfield" style="left:231px;top:2530px;width:747px;height:126px">Text here...</div>
  <div class="btn contact-submit">Submit</div>

  <h2 class="section-title serif gallery-title">GALLERY</h2>
  <div class="shot" style="left:144px;top:3045px;width:216px;height:427px;background:linear-gradient(180deg,#9cc3e6 0%,#5f8a3a 50%,#7db43a 100%)" role="img" aria-label="Photo of a patio seating area beside a lawn and stone path"></div>
  <div class="shot" style="left:376px;top:3045px;width:448px;height:206px;background:linear-gradient(180deg,#cfe0ee 0%,#3d6b2a 40%,#6fae34 100%)" role="img" aria-label="Photo of outdoor lounge furniture on a garden lawn"></div>
  <div class="shot" style="left:840px;top:3045px;width:215px;height:206px;background:linear-gradient(180deg,#4a3a2e 0%,#5c6b3a 55%,#78a83a 100%)" role="img" aria-label="Photo of a gardener laying new turf"></div>
  <div class="shot" style="left:376px;top:3268px;width:216px;height:204px;background:linear-gradient(180deg,#4f7a34 0%,#7c9a4a 60%,#a08a6a 100%)" role="img" aria-label="Photo of planted beds along a low brick wall"></div>
  <div class="shot" style="left:607px;top:3268px;width:447px;height:204px;background:linear-gradient(180deg,#6e9a3a 0%,#a87a5a 55%,#86a84a 100%)" role="img" aria-label="Photo of a curved brick patio with garden lamps"></div>

  <div class="footer-brand">BRINDMOOR<small>GARDENING</small></div>
  <div class="fcol" style="left:464px">
    <h4>Quick Links</h4>
    <ul><li>Home</li><li>About</li><li>Services</li><li>Showcase</li><li>Contact</li></ul>
  </div>
  <div class="fcol" style="left:647px">
    <h4>Resources</h4>
    <ul><li>Contact</li><li>Blog</li><li>Info</li><li>Account</li></ul>
  </div>
  <div class="fcol" style="left:816px;width:230px">
    <h4>Contact Us</h4>
    <div class="contact-item"><i><svg width="12" height="14" viewBox="0 0 12 14" aria-hidden="true"><path d="M6 0a5 5 0 0 0-5 5c0 4 5 9 5 9s5-5 5-9a5 5 0 0 0-5-5z" fill="#fff"/><circle cx="6" cy="5" r="2" fill="#c39437"/></svg></i><span>48 Alder Crescent, Westbrook Hills</span></div>
    <div class="contact-item"><i><svg width="13" height="13" viewBox="0 0 24 24" aria-hidden="true"><path d="M6.6 10.8a15.1 15.1 0 0 0 6.6 6.6l2.2-2.2c.3-.3.7-.4 1-.2 1.1.4 2.3.6 3.6.6.6 0 1 .4 1 1V20c0 .6-.4 1-1 1A17 17 0 0 1 3 4c0-.6.4-1 1-1h3.5c.6 0 1 .4 1 1 0 1.3.2 2.5.6 3.6.1.3 0 .7-.2 1z" fill="#fff"/></svg></i><span style="padding-top:5px">555-318-4062</span></div>
    <div class="contact-item"><i><svg width="13" height="10" viewBox="0 0 13 10" aria-hidden="true"><rect width="13" height="10" fill="#fff"/><polyline points="0,0 6.5,5 13,0" fill="none" stroke="#c39437"/></svg></i><span style="padding-top:5px">hello@brindmoorgardens.com</span></div>
  </div>
  <div class="rule"></div>
  <div class="copyright">© Copyrights 2024 | All Rights Reserved</div>

</div>
</body>
</html>
```